Waterjet Cutting Business requires an up to date website

We currently have a website which is outdated and in need of modernization.
We are only looking for a simple website with around 4 pages: Home, Contact Us, Materials, Gallery.
We have some pictures and a logo which can be used.
Our primary business is profile cutting of materials to customers specifications using high-pressure water with abrasive.
We are looking for creative ideas and are open to suggestions!
http://brightfordcutworks.com/index.asp?pid=1
Update:
Cut quality picture (uploaded)
Map
Comparison to other profile cutting methods such as plasma/laser
Single page style without continuous scrolling
"We can cut virtually any material from any drawing whether it be a Full 3D cad models to hand sketched "
Target Market(s)
Film Industry, Prototype, Engineering, Architect, Artisits, one off designs
Industry/Entity Type
Engineering
Number of Pages Required
1 page
Font styles to use
Look and feel

```html
<!DOCTYPE html>
<html lang="en">
<head>
<meta charset="utf-8">
<title>Brightford Cutworks – Waterjet Profile Cutting</title>
<link href="https://fonts.googleapis.com/css2?family=Oswald:wght@400;500&family=Open+Sans:wght@400;600&display=swap" rel="stylesheet">
<style>
:root{
  --orange:#f26a1b;
  --blue:#1c6396;
  --ink:#333;
  --muted:#555;
  --topbar:#f4f4f4;
  --blush:#fcf7f7;
  --charcoal:#3d3b3b;
  --footer:#262525;
  --footer-base:#1b1a1a;
  --white:#fff;
}
*{box-sizing:border-box;margin:0;padding:0}
html,body{width:1200px;height:2459px;overflow:hidden}
body{font-family:"Open Sans",Arial,sans-serif;color:var(--ink);background:var(--white);position:relative}
.abs{position:absolute}
.heading{font-family:"Oswald",Arial,sans-serif;font-weight:400;text-transform:uppercase;letter-spacing:.5px}
.rule{width:50px;height:3px;background:var(--orange)}
.btn{display:flex;align-items:center;justify-content:center;font-size:12px;letter-spacing:.5px}

/* top bar */
.topbar{top:0;left:0;width:1200px;height:36px;background:var(--topbar);font-size:11px;color:#444}
.topbar .item{top:11px;display:flex;align-items:center;gap:7px}
.topbar .socials{top:13px;left:980px;display:flex;gap:6px}
.topbar .socials span{width:9px;height:9px;border-radius:50%;background:var(--orange)}

/* header */
.header{top:36px;left:0;width:1200px;height:79px;background:var(--white);box-shadow:0 1px 3px rgba(0,0,0,.08)}
.brand{left:160px;top:22px;display:flex;align-items:center;gap:10px}
.brand .mark{width:26px;height:26px;background:var(--blue)}
.brand .name{font-family:"Oswald",Arial,sans-serif;font-weight:500;font-size:24px;color:var(--blue);letter-spacing:1px}
.nav{left:510px;top:30px;display:flex;font-size:11px;text-transform:uppercase;color:#333}
.nav a{padding:0 20px;border-left:1px solid #ddd;color:inherit;text-decoration:none}
.nav a:first-child{border-left:none;color:var(--blue)}
.quote-btn{left:910px;top:17px;width:129px;height:33px;background:var(--orange);color:var(--white);font-weight:600;font-size:12px;gap:6px}

/* hero */
.hero{top:115px;left:0;width:1200px;height:431px;background:linear-gradient(100deg,#5f6668 0%,#8e9496 35%,#7b8082 60%,#3d4a5a 85%,#6a5140 100%)}
.hero .shade{inset:0;background:rgba(20,22,26,.35)}
.hero-frame{left:333px;top:78px;width:536px;height:254px}
.hero-title{top:95px;left:0;width:1200px;text-align:center;color:var(--white);font-size:31px;letter-spacing:1px}
.hero .rule{left:575px;top:150px;width:50px}
.hero-text{top:182px;left:390px;width:420px;text-align:center;color:var(--white);font-size:12px;line-height:19px}
.hero-btn-primary{left:503px;top:262px;width:104px;height:30px;background:var(--blue);color:var(--white);text-transform:uppercase;font-size:11px}
.hero-btn-outline{left:617px;top:262px;width:104px;height:30px;border:2px solid var(--white);color:var(--white);text-transform:uppercase;font-size:11px}
.hero-arrow{top:184px;width:31px;height:29px;background:rgba(120,110,100,.75);border:1px solid #ccc}

/* welcome */
.welcome{top:546px;left:0;width:1200px;height:314px;background:var(--blush)}
.section-title{left:0;width:1200px;text-align:center;font-size:26px;color:#333}
.section-title em{font-style:normal;color:var(--blue)}
.welcome-photo{left:164px;top:110px;width:385px;height:167px;background:linear-gradient(90deg,#9fb8c6,#c5d3dc 50%,#6a8aa3);border:4px solid var(--white);box-shadow:0 0 3px rgba(0,0,0,.15)}
.welcome-text{left:572px;top:103px;width:468px;font-size:12.5px;line-height:20px;color:var(--muted);text-align:justify}
.read-more{left:572px;top:234px;width:107px;height:38px;border:1px solid #bbb;background:var(--white);color:#555;font-size:13px}

/* materials */
.materials{top:860px;left:0;width:1200px;height:248px}
.materials-copy{left:0;top:0;width:554px;height:248px;background:var(--charcoal);color:var(--white)}
.materials-title{left:160px;top:12px;font-size:25px;color:var(--white)}
.materials-text{left:160px;top:58px;width:363px;font-size:11.5px;line-height:17.5px}
.materials-text p+p{margin-top:8px}
.details-btn{left:160px;top:183px;width:122px;height:38px;border:2px solid #ccc;color:var(--white);text-transform:uppercase}
.materials-visual{left:554px;top:0;width:646px;height:248px;background:linear-gradient(90deg,#8a4a1e,#c86a28 50%,#b25c22)}
.material-shot{top:31px;width:229px;height:162px;border:2px solid #f0e0d0}

/* gallery */
.gallery-title{top:1130px}
.gallery-rule{left:575px;top:1178px}
.filters{top:1211px;left:0;width:1200px;display:flex;justify-content:center;gap:33px;font-size:12.5px;color:#555;text-transform:uppercase}
.filters .active{color:var(--blue)}
.gallery{top:1260px;left:0;width:1200px;height:453px;display:grid;grid-template-columns:291px 304px 303px 302px;grid-template-rows:227px 226px}
.tile{position:relative}
.tile-overlay{inset:0;background:rgba(230,110,30,.55);display:flex;align-items:center;justify-content:center}
.tile-overlay .frame{position:absolute;inset:16px;border:1px solid rgba(255,255,255,.6)}
.tile-overlay .btn{width:112px;height:38px;border:2px solid var(--white);color:var(--white);font-size:17px;position:relative}

/* contact */
.contact-title{top:1733px}
.contact-rule{left:575px;top:1785px}
.map{top:1827px;left:0;width:688px;height:302px;background:linear-gradient(135deg,#e9ebe6,#dfe4dc 50%,#e7e6df)}
.contact-info{top:1827px;left:688px;width:512px;height:302px;border-top:1px solid #e5e5e5;border-left:1px solid #e5e5e5}
.info-row{left:77px;display:flex;gap:14px;font-size:12px;line-height:22px;color:#444}
.info-row svg{flex:none;margin-top:5px}

/* footer */
.footer{top:2129px;left:0;width:1200px;height:289px;background:linear-gradient(180deg,#2f2d2c,var(--footer))}
.footer-title{top:36px;font-size:21px;color:var(--white);letter-spacing:1px}
.footer-line{top:74px;height:1px;background:#555}
.footer-line i{display:block;width:50px;height:3px;margin-top:-1px;background:#e33}
.hours{left:160px;top:90px;font-size:11.5px;line-height:23.5px;color:var(--white)}
.links{left:487px;top:88px;width:227px;font-size:11.5px;color:var(--white)}
.links li{list-style:none;padding:0 5px;height:28.5px;line-height:25px;border-bottom:1px dotted #777}
.links li:last-child{border-bottom:none}
.footer-info .row{left:765px;display:flex;gap:14px;font-size:11.5px;line-height:17px;color:var(--white)}
.footer-social{left:160px;top:226px;display:flex;gap:11px}
.footer-social span{width:25px;height:25px;border-radius:50%;background:var(--white)}
.footer-base{top:2418px;left:0;width:1200px;height:41px;background:var(--footer-base);color:#ddd;font-size:11.5px;padding:14px 160px}
.footer-base b{font-weight:400;color:#e33}
</style>
</head>
<body>

<!-- top bar -->
<div class="abs topbar">
  <div class="abs item" style="left:160px">
    <svg width="10" height="10" viewBox="0 0 24 24"><path fill="#f26a1b" d="M6.6 10.8a15 15 0 006.6 6.6l2.2-2.2a1 1 0 011-.25 11.4 11.4 0 003.6.6 1 1 0 011 1V20a1 1 0 01-1 1A17 17 0 013 4a1 1 0 011-1h3.5a1 1 0 011 1c0 1.25.2 2.45.57 3.57a1 1 0 01-.25 1z"/></svg>
    +01632 960418
  </div>
  <div class="abs item" style="left:276px">
    <svg width="11" height="9" viewBox="0 0 24 18"><path fill="#f26a1b" d="M0 0h24v18H0z"/><path fill="none" stroke="#f4f4f4" stroke-width="2" d="M1 1l11 9 11-9"/></svg>
    info@brightfordcutworks.com
  </div>
  <div class="abs socials"><span></span><span></span><span></span><span></span></div>
</div>

<!-- header -->
<header class="abs header">
  <div class="abs brand"><span class="mark"></span><span class="name">BRIGHTFORD</span></div>
  <nav class="abs nav"><a href="#">Home</a><a href="#">Materials</a><a href="#">Gallery</a><a href="#">Contact Us</a></nav>
  <div class="abs btn quote-btn">
    <svg width="11" height="9" viewBox="0 0 24 18"><path fill="#fff" d="M0 0h24v18H0z"/><path fill="none" stroke="#f26a1b" stroke-width="2" d="M1 1l11 9 11-9"/></svg>
    GET A QUITE
  </div>
</header>

<!-- hero -->
<section class="abs hero" role="img" aria-label="Photograph of a waterjet cutting head spraying water over a metal workpiece">
  <div class="abs shade"></div>
  <svg class="abs hero-frame" viewBox="0 0 536 254" fill="none" stroke="#fff" stroke-width="3">
    <path d="M2 40V2h38M496 2h38v38M534 214v38h-38M40 252H2v-38"/>
  </svg>
  <h1 class="abs heading hero-title">Engineering Your Dreams With Us</h1>
  <div class="abs rule"></div>
  <p class="abs hero-text">Temporibus autem quibusdam et aut officiis debitis is aut rerum ne-cessitatibus saepe eveniet ut et seo lage voluptates</p>
  <div class="abs btn hero-btn-primary">Our History</div>
  <div class="abs btn hero-btn-outline">View Project</div>
  <div class="abs hero-arrow" style="left:20px"><svg width="29" height="27" viewBox="0 0 29 27"><path d="M16 10l-4 3.5 4 3.5" fill="none" stroke="#fff" stroke-width="1.5"/></svg></div>
  <div class="abs hero-arrow" style="left:1145px"><svg width="29" height="27" viewBox="0 0 29 27"><path d="M13 10l4 3.5-4 3.5" fill="none" stroke="#fff" stroke-width="1.5"/></svg></div>
</section>

<!-- welcome -->
<section class="abs welcome">
  <h2 class="abs heading section-title" style="top:33px">Welcome to <em>Brightford Cutworks</em></h2>
  <div class="abs rule" style="left:575px;top:78px"></div>
  <div class="abs welcome-photo" role="img" aria-label="Photograph of two colleagues reviewing work at an office desk"></div>
  <p class="abs welcome-text">Lorem ipsum dolor sit amet, consectetur adipiscing elit. Cras mollis, leo a condimen tum vehicula, dui tellus mattis libero, et aliquet nisl tortor quis velit. Proin eget neque ut erat commodo consequat sit amet vitae velit maecenas lacinia mattis. Lorem ipsum dolor sit amet, consectetur adipiscing elit. tortor quis velit. lacinia mattis. Lorem ipsum dolor sit amet, consectetur.</p>
  <div class="abs btn read-more">Read More</div>
</section>

<!-- materials -->
<section class="abs materials">
  <div class="abs materials-copy">
    <h2 class="abs heading materials-title">Our Materials</h2>
    <div class="abs materials-text">
      <p>It is a long established fact that a reader will be distracted by the readable content of a page when looking at its layout. It is a long established fact that a reader will be distracted its layout.</p>
      <p>It is a long established fact that a reader will be distracted by the readable content of a page.</p>
    </div>
    <div class="abs btn details-btn">View Details</div>
  </div>
  <div class="abs materials-visual" role="img" aria-label="Close-up photograph of a textured orange metal sheet">
    <div class="abs material-shot" style="left:15px;background:linear-gradient(135deg,#2a2a2e,#5a5a60 50%,#c0704a)" role="img" aria-label="Photograph of a cutting head piercing a perforated steel plate"></div>
    <div class="abs material-shot" style="left:259px;background:linear-gradient(135deg,#7a1a7a,#e040c8 50%,#5a1060)" role="img" aria-label="Photograph of a cutting head over a plate under magenta light"></div>
  </div>
</section>

<!-- gallery -->
<h2 class="abs heading section-title gallery-title">Our <em>Gallery</em></h2>
<div class="abs rule gallery-rule"></div>
<div class="abs filters"><span class="active">All</span><span>MS Profile Cutting Service</span><span>Profile Cutting Works</span><span>Steel Cutting Service</span></div>
<section class="abs gallery">
  <div class="tile" style="background:linear-gradient(135deg,#3a3230,#6a5a52 50%,#c8b8a8)" role="img" aria-label="Photograph of a cutting nozzle throwing sparks"></div>
  <div class="tile" style="background:linear-gradient(135deg,#2a2c30,#7a7c84 50%,#3a3c40)" role="img" aria-label="Photograph of a cutting head over a perforated plate"></div>
  <div class="tile" style="background:linear-gradient(135deg,#8a4a20,#d07030 50%,#a05020)" role="img" aria-label="Photograph of a cutting head over an orange-lit workpiece">
    <div class="abs tile-overlay"><div class="frame"></div><div class="btn">Click Here</div></div>
  </div>
  <div class="tile" style="background:linear-gradient(135deg,#0a1a1a,#1a6a6a 50%,#0a2a2a)" role="img" aria-label="Photograph of a cutting head over a teal-lit grid bed"></div>
  <div class="tile" style="background:linear-gradient(135deg,#6a106a,#e030c0 50%,#4a0a4a)" role="img" aria-label="Photograph of a cutting head over a magenta-lit grid bed"></div>
  <div class="tile" style="background:linear-gradient(135deg,#0a1a4a,#2a4aa0 50%,#101a3a)" role="img" aria-label="Photograph of a cutting head over a blue-lit plate"></div>
  <div class="tile" style="background:linear-gradient(135deg,#1a2228,#3a4a52 50%,#10161a)" role="img" aria-label="Photograph of twin cutting heads over a dark plate"></div>
  <div class="tile" style="background:linear-gradient(135deg,#0a2a0a,#2a9a3a 50%,#0a3a10)" role="img" aria-label="Photograph of twin cutting heads under green light"></div>
</section>

<!-- contact -->
<h2 class="abs heading section-title contact-title">Contact <em>Us</em></h2>
<div class="abs rule contact-rule"></div>
<div class="abs map" role="img" aria-label="Street map showing the workshop location in the business park"></div>
<section class="abs contact-info">
  <div class="abs info-row" style="top:62px">
    <svg width="14" height="12" viewBox="0 0 24 20"><path fill="#f26a1b" d="M12 0l12 10h-3v10h-6v-6H9v6H3V10H0z"/></svg>
    <span>Unit 7, Kestrel Court, Marlow Way, Ashdown Trade<br>Park, Brightford, Bucks, BF4 2QT.</span>
  </div>
  <div class="abs info-row" style="top:124px">
    <svg width="12" height="12" viewBox="0 0 24 24"><path fill="#f26a1b" d="M6.6 10.8a15 15 0 006.6 6.6l2.2-2.2a1 1 0 011-.25 11.4 11.4 0 003.6.6 1 1 0 011 1V20a1 1 0 01-1 1A17 17 0 013 4a1 1 0 011-1h3.5a1 1 0 011 1c0 1.25.2 2.45.57 3.57a1 1 0 01-.25 1z"/></svg>
    <span>+ 01632 960418</span>
  </div>
  <div class="abs info-row" style="top:159px">
    <svg width="14" height="11" viewBox="0 0 24 18"><path fill="#f26a1b" d="M0 0h24v18H0z"/><path fill="none" stroke="#fff" stroke-width="2" d="M1 1l11 9 11-9"/></svg>
    <span>info@brightfordcutworks.com</span>
  </div>
  <div class="abs info-row" style="top:194px">
    <svg width="13" height="13" viewBox="0 0 24 24"><circle cx="12" cy="12" r="11" fill="#f26a1b"/><path d="M1 12h22M12 1c-4 4-4 18 0 22M12 1c4 4 4 18 0 22" fill="none" stroke="#fff" stroke-width="1.5"/></svg>
    <span>www.brightfordcutworks.com</span>
  </div>
</section>

<!-- footer -->
<footer class="abs footer">
  <h3 class="abs heading footer-title" style="left:160px">Business Hours</h3>
  <div class="abs footer-line" style="left:160px;width:262px"><i></i></div>
  <div class="abs hours">Sunday to Tuesday: 8am to 6pm<br>Saturday: 9am to 4pm<br>Friday: Closed<br>Support Hours is 24/7 every day</div>
  <div class="abs footer-social"><span></span><span></span><span></span><span></span></div>

  <h3 class="abs heading footer-title" style="left:487px">Quick Link</h3>
  <div class="abs footer-line" style="left:487px;width:227px"><i></i></div>
  <ul class="abs links"><li>Home</li><li>Materials</li><li>Gallery</li><li>Contact Us</li></ul>

  <h3 class="abs heading footer-title" style="left:760px">Contact Info</h3>
  <div class="abs footer-line" style="left:760px;width:280px"><i></i></div>
  <div class="footer-info">
    <div class="abs row" style="top:90px">
      <svg width="13" height="11" viewBox="0 0 24 20" style="margin-top:3px;flex:none"><path fill="#fff" d="M12 0l12 10h-3v10h-6v-6H9v6H3V10H0z"/></svg>
      <span>Unit 7, Kestrel Court, Marlow Way, Ashdown<br>Trade Park, Brightford, Bucks,<br>BF4 2QT</span>
    </div>
    <div class="abs row" style="top:166px">
      <svg width="11" height="11" viewBox="0 0 24 24" style="margin-top:3px;flex:none"><path fill="#fff" d="M6.6 10.8a15 15 0 006.6 6.6l2.2-2.2a1 1 0 011-.25 11.4 11.4 0 003.6.6 1 1 0 011 1V20a1 1 0 01-1 1A17 17 0 013 4a1 1 0 011-1h3.5a1 1 0 011 1c0 1.25.2 2.45.57 3.57a1 1 0 01-.25 1z"/></svg>
      <span>01632 960418</span>
    </div>
    <div class="abs row" style="top:200px">
      <svg width="13" height="10" viewBox="0 0 24 18" style="margin-top:4px;flex:none"><path fill="#fff" d="M0 0h24v18H0z"/><path fill="none" stroke="#262525" stroke-width="2" d="M1 1l11 9 11-9"/></svg>
      <span>info@brightfordcutworks.com</span>
    </div>
  </div>
</footer>
<div class="abs footer-base">© 2018 <b>brightfordcutworks.com</b> All Rights Reserved.</div>

</body>
</html>
```